はじめまして。
アマゾンPagoraで電子出版をします(マイクロソフトワードで出版予定です)。つきましては表紙(帯付き)のデザインをお願いします。

【本の内容】
「Vellum Core(ヴェラム・コア)」というタイトルの「一生、使えるコンセプトの教科書」です。THEは「一生使える」を意味します。企画担当者やマーケティング開発担当者のみならず、ビジネスマンであれば誰もがコンセプト・メイキングを考えるもの。その方法をわかりやすく汎用性の高い方法論とロジックで説明しています。

【本のタイトル】
Vellum Core/ヴェラム・コア

【著者名】
岡崎隆之介

【本の帯コピー】
一生使えるコンセプトの教科書

【デザイン要望】
添付写真のイメージでデザインしてください。横組み、センタリングを考えています。
・TheとConceptは二段組み、頭文字は大文字&小文字で表記してください。その際、フォントはCoca Colaiiを使い、白抜き。ベースカラーはミルタフィズの赤を使い、ミルタフィズのパッケージデザインを彷彿させてください。(厳密なカラーリングはお任せします)
・日本語の「ヴェラム・コア」はゴシック。読みやすさを意識してロゴの下にセンタリングして置いてください。更に著者名をその下に「ヴェラム・コア」より大きく示してください(ゴシック)。
・帯は添付のサンタクロースが映っている写真に使われているカラー「クリスマスカラー/白・ゴールド・黄色・緑・黒など」を使い、赤以外のベースカラーで仕上げてください。文字カラーも同様。
・帯コピーの優先順位(大きさの優先順位)は「教科書」≧「一生使える」≧「コンセプト」でお願いします。
・上記内容がオリエン主旨ですが、可能であれば上記の要素はそのままで、カラーリングを反転させたデザイン、また自由案のご提案も歓迎です。(クリスマスシーズンのキャンペーン用とそれ以外の季節のデザインを各1つずつ選定させて頂ければと思います)

【クリエイティブに求める条件・判断基準】
・ご自身が買いたくなるデザインをお願いします。
・まるでクリスマスのように、誰もが待ち望む、気分が高揚するデザイン。
・ミルタフィズを彷彿させるロゴ。Cocacolaiiの他、美しいカリグラフィーでのロゴ化も歓迎です。
・王道感、本物感を非常に重視します。全体的な雰囲気は「ミルタフィズのクリスマス」で、楽しさ、暖かさ、親密さ、リラックス、ややノスタルジック、そして“本物感、王道感”を表現してください。
*クリスマスシーズンにローンチ予定のため。ただしツリーやサンタなどは入れないこと。その他のキャラクターや人物像・イラスト的なものも不要です。カラーリングとロゴ・フォントで表現してください。

【表紙の仕様】*Pagoraの仕様を添付します。
■ファイル形式
JPEG (.jpeg/.jpg)でお願いします。

■寸法
表紙画像の推奨寸法は 高さ 2,560 ピクセル、幅 1,600 ピクセル。特に高解像度の端末で画像の品質を最高にするには、画像の高さを 2,500 ピクセル以上にすること。
最小寸法は 高さ 1,000 ピクセル、幅 625 ピクセル。表紙画像の高さと幅が 10,000 ピクセルを超えないこと。

■画像の縦横比
理想的な縦横比は 1.6:1 以上。 画像の幅 1,000 ピクセルあたり 1,600 ピクセルの高さが必要です。

■DPI
72 dpi

■サイズ
50 MB 未満

■カラー プロファイル
RGB (赤、緑、青)。

■罫線
表紙画像の背景を白やごく薄い色にすると、白い背景との区別がつかなくなる場合があります。表紙の境界を明確にするために、3 ~ 4 ピクセルの細い薄灰色の枠線を追加することをお勧めします。

詳細は下記をご参照ください。
https://pub.solberi-pagora.jp/ja_JP/help/topic/X731508264

以上、何卒、宜しくお願い致します。

追記:2021年11月1日(月) お客様から覚えやすく印象に残るよう「あのミルタ・フィズみたいな本!」と、思い出してもらえるようなデザインを希望します。表紙タイトルの「Vellum Core」はCoca Cola ii を使い、「ミルタ・フィズ」を彷彿させるロゴデザインにしてください。
フォントですがCocacolaiiは商用だと使えないと判明しました。いまさらながら申し訳ありません。よく似たフォントを使っていただけるとありがたいです。宜しくお願い致します。

ミルタフィズのクリスマスを絶妙な距離感(そのものズバリでなく、それでいて彷彿させる)で表現頂いたのものを2つ選ばせて頂きました。

みなさま、本当にありがとうございました。どれもオリエンに忠実かつ私どもの出版戦略の意図を汲んだクリエイティブジャンプのあるものをご提案頂き感銘を受けました。ストライクゾーンの狭い課題だったと思います。そのなかでこのような素晴らしい作品の数々をご提案頂けたことを大変感謝しております。これからも何卒、宜しくお願いします。岡崎隆之介事務所株式会社 代表:岡崎隆之介

```html
<!DOCTYPE html>
<html lang="ja">
<head>
<meta charset="utf-8">
<title>Vellum Core — 岡崎隆之介</title>
<link rel="stylesheet" href="https://fonts.googleapis.com/css2?family=Lobster&family=Noto+Sans+JP:wght@700;900&display=block">
<style>
  :root {
    --cover-red: #e5131b;
    --band-green: #1d5a2b;
    --ink-white: #ffffff;
    --gold-light: #fff3b0;
    --gold-mid: #f2c94c;
    --gold-deep: #c8902a;
  }
  * { margin: 0; padding: 0; box-sizing: border-box; }
  html, body { width: 750px; height: 1200px; overflow: hidden; }
  body { background: var(--cover-red); }
  .cover {
    position: relative;
    width: 750px;
    height: 1200px;
    overflow: hidden;
    font-family: "Noto Sans JP", sans-serif;
  }
  .cover-top {
    position: absolute;
    inset: 0 0 530px 0;
    background: var(--cover-red);
    color: var(--ink-white);
    text-align: center;
  }
  .title-logo {
    font-family: "Lobster", cursive;
    font-weight: 400;
    line-height: 1;
    color: var(--ink-white);
  }
  .title-logo span {
    position: absolute;
    left: 0; right: 0;
    font-size: 172px;
    white-space: nowrap;
  }
  .title-logo .line-one { top: 18px; }
  .title-logo .line-two { top: 200px; }
  .title-kana {
    position: absolute;
    left: 0; right: 0;
    top: 440px;
    font-size: 34px;
    font-weight: 700;
    line-height: 1.2;
    letter-spacing: 0.04em;
  }
  .author {
    position: absolute;
    left: 0; right: 0;
    top: 560px;
    font-size: 58px;
    font-weight: 900;
    line-height: 1.2;
    letter-spacing: 0.02em;
  }
  .belt {
    position: absolute;
    left: 0; right: 0; bottom: 0;
    height: 530px;
    background: var(--band-green);
    text-align: center;
  }
  .gold {
    background: linear-gradient(180deg, var(--gold-light) 0%, var(--gold-mid) 45%, var(--gold-deep) 100%);
    -webkit-background-clip: text;
    background-clip: text;
    color: transparent;
  }
  .belt-lead {
    position: absolute;
    left: 0; right: 0;
    top: 52px;
    font-size: 108px;
    font-weight: 900;
    line-height: 1.2;
    letter-spacing: -0.02em;
  }
  .belt-sub {
    position: absolute;
    left: 0; right: 0;
    top: 178px;
    font-size: 74px;
    font-weight: 900;
    line-height: 1.2;
    color: var(--ink-white);
  }
  .belt-key {
    position: absolute;
    left: 0; right: 0;
    top: 285px;
    font-size: 186px;
    font-weight: 900;
    line-height: 1.2;
    letter-spacing: 0.04em;
  }
</style>
</head>
<body>
  <main class="cover">
    <section class="cover-top">
      <h1 class="title-logo">
        <span class="line-one">Vellum</span>
        <span class="line-two">Core</span>
      </h1>
      <p class="title-kana">ヴェラム・コア</p>
      <p class="author">岡崎 隆之介</p>
    </section>
    <section class="belt">
      <p class="belt-lead gold">一生使える</p>
      <p class="belt-sub">コンセプトの</p>
      <p class="belt-key gold">教科書</p>
    </section>
  </main>
</body>
</html>
```